Coastal Gin Label Design

We are needing a nautical/coastal themed label for our upcoming gin release.

We have saltbush, cucumber, juniper, and quandong being used in this gin.

Name of the Gin; Harbor Glow

The logo attached is the company logo, but doesn't have to be used on the front of the label, ie it can just be the name Fernwhistle somewhere on the front.
Bottle specs attached as well so you can accurately represent the bottle- this bottle is also clear.

Target Market(s)

Women 25- 45

Font styles to use
Serif
Decorative

Colors
d5edf4
86cae7
33a6d7
86cfc6
cfeae6
ffffff
f6faec
ecf7fb
fefeff

Requirements
Must have
• Ocean/Coastal vibe to the label
Nice to have
• Blues,Whites clean and crisp
Should not have
• No generic word art look to it.
A dark mood

```html
<!DOCTYPE html>
<html lang="en">
<head>
<meta charset="utf-8">
<title>Harbor Glow Gin – Label</title>
<link rel="stylesheet" href="https://fonts.googleapis.com/css2?family=Bodoni+Moda:opsz,wght@6..96,400;6..96,500&family=Cormorant+Garamond:wght@500;600&family=Oswald:wght@300&display=swap">
<style>
  :root {
    --backdrop: #f9f5f0;
    --label-white: #fefeff;
    --mist: #ecf7fb;
    --sky-pale: #d5edf4;
    --sky: #86cae7;
    --sea: #33a6d7;
    --ink-blue: #3f6f98;
    --ink-deep: #2f5f86;
    --wheel-tint: #e4eef3;
  }
  * { margin: 0; padding: 0; box-sizing: border-box; }
  html, body {
    width: 849px;
    height: 1200px;
    overflow: hidden;
    background: var(--backdrop);
  }
  .canvas {
    position: relative;
    width: 849px;
    height: 1200px;
    display: flex;
    align-items: center;
    justify-content: center;
  }
  .label {
    position: relative;
    width: 700px;
    height: 770px;
    background: linear-gradient(180deg, var(--label-white) 0%, var(--mist) 100%);
    overflow: hidden;
    box-shadow: 0 0 0 1px #ebe6df;
  }
  .wash {
    position: absolute;
    left: 0;
    right: 0;
    bottom: 0;
    height: 470px;
    background:
      linear-gradient(180deg,
        rgba(213,237,244,0) 0%,
        rgba(213,237,244,0.85) 22%,
        rgba(134,202,231,0.75) 48%,
        rgba(213,237,244,0.9) 62%,
        rgba(134,202,231,0.85) 78%,
        rgba(51,166,215,0.55) 100%);
  }
  .wheel-motif {
    position: absolute;
    left: 330px;
    top: 150px;
    width: 250px;
    height: 250px;
    border-radius: 50%;
    background: radial-gradient(circle, var(--wheel-tint) 0%, rgba(228,238,243,0) 70%);
  }
  .maker {
    position: absolute;
    top: 92px;
    left: 0;
    right: 0;
    display: flex;
    align-items: center;
    justify-content: center;
    gap: 12px;
  }
  .maker-dot {
    width: 14px;
    height: 14px;
    border-radius: 50%;
    background: var(--ink-deep);
  }
  .maker-name {
    font-family: "Cormorant Garamond", serif;
    font-weight: 600;
    font-size: 30px;
    letter-spacing: 2px;
    color: var(--ink-deep);
  }
  .gin-name {
    position: absolute;
    top: 220px;
    left: 0;
    right: 0;
    text-align: center;
    font-family: "Bodoni Moda", serif;
    font-weight: 400;
    color: var(--ink-blue);
    line-height: 0.9;
  }
  .gin-name-line {
    display: block;
    font-size: 150px;
    letter-spacing: -3px;
  }
  .gin-name-line.second { margin-left: 40px; }
  .spirit {
    position: absolute;
    top: 545px;
    left: 0;
    right: 0;
    text-align: center;
    font-family: "Oswald", sans-serif;
    font-weight: 300;
    font-size: 26px;
    letter-spacing: 18px;
    padding-left: 18px;
    color: var(--ink-blue);
  }
  .volume {
    position: absolute;
    top: 690px;
    left: 0;
    right: 0;
    text-align: center;
    font-family: "Oswald", sans-serif;
    font-weight: 300;
    font-size: 20px;
    letter-spacing: 1px;
    color: var(--ink-deep);
  }
</style>
</head>
<body>
  <main class="canvas">
    <section class="label">
      <div class="wash" role="img" aria-label="Soft watercolour wash of layered blue ocean waves"></div>
      <div class="wheel-motif" role="img" aria-label="Faint ship's wheel motif"></div>
      <div class="maker">
        <span class="maker-dot"></span>
        <span class="maker-name">FERNWHISTLE</span>
      </div>
      <h1 class="gin-name">
        <span class="gin-name-line">Harbor</span>
        <span class="gin-name-line second">Glow</span>
      </h1>
      <p class="spirit">GIN</p>
      <p class="volume">500ml | 37.5% ABV</p>
    </section>
  </main>
</body>
</html>
```